Corva Linde Christmas Card 2025

I need a Christmas card design for Corva Linde (www.corvalinde.com). My client loves everything Maren Quill. I’ve attached this year’s inspirations, including the live wreath she is gifting and the brand guidelines. She prefers the softer colors shown in the inspiration materials. The greeting should read Merry Christmas (not Happy Holidays). The final design should feel elegant, festive, and aligned with the Corva Linde brand.”

```html
<!DOCTYPE html>
<html lang="en">
<head>
<meta charset="utf-8">
<title>Corva Linde Christmas Card 2025</title>
<link rel="stylesheet" href="https://fonts.googleapis.com/css2?family=Montserrat:wght@300;400;500&display=swap">
<style>
  :root {
    --backdrop: #e4e4e4;
    --inside-paper: #f6f5f4;
    --inside-shade: #ebebeb;
    --pattern-tint: #efeeed;
    --cover-paper: #ffffff;
    --blush: #f6e4dd;
    --blush-pattern: #f3ddd5;
    --swirl-tint: #f8efeb;
    --photo-tone: #a9b39a;
    --photo-tone-deep: #8e9a7e;
    --orange: #f07e2b;
    --orange-soft: #f3a47a;
    --brown: #5a3b2e;
    --brand-grey: #7a6a66;
    --brand-orange: #ee9a57;
  }
  * { box-sizing: border-box; margin: 0; padding: 0; }
  html, body {
    width: 1200px; height: 1200px; overflow: hidden;
    background: var(--backdrop);
    font-family: "Montserrat", sans-serif;
  }
  .card-spread {
    position: absolute; left: 119px; top: 238px;
    width: 993px; height: 695px;
    display: flex;
  }
  .panel { position: relative; height: 695px; overflow: hidden; }

  /* Inside panel */
  .panel--inside {
    width: 496px;
    background: linear-gradient(90deg, var(--inside-paper) 0%, #f3f3f3 80%, var(--inside-shade) 100%);
  }
  .pattern-field {
    position: absolute; inset: 0;
    background: linear-gradient(180deg, var(--pattern-tint) 0%, rgba(239,238,237,0.4) 100%);
  }
  .brand-lockup {
    position: absolute; left: 184px; top: 320px;
    display: flex; align-items: center; gap: 12px;
  }
  .brand-dot { width: 55px; height: 55px; border-radius: 50%; background: var(--brand-orange); }
  .brand-name {
    color: var(--brand-grey); font-weight: 300; font-size: 23px;
    letter-spacing: 2px; line-height: 25px; text-transform: uppercase;
  }

  /* Cover panel */
  .panel--cover { width: 497px; background: var(--cover-paper); }
  .blush-band {
    position: absolute; left: 79px; top: 0; width: 347px; height: 440px;
    background: linear-gradient(180deg, var(--blush-pattern) 0%, var(--blush) 60%, rgba(246,228,221,0) 100%);
  }
  .swirl-field {
    position: absolute; left: 0; top: 445px; width: 497px; height: 250px;
    background: linear-gradient(180deg, rgba(248,239,235,0) 0%, var(--swirl-tint) 100%);
  }
  .greeting { position: absolute; left: 79px; top: 0; width: 347px; text-align: center; }
  .greeting__lead {
    margin-top: 43px; font-size: 10px; font-weight: 500; line-height: 12px;
    letter-spacing: 6.5px; color: var(--brown); padding-left: 6px;
  }
  .greeting__merry {
    margin-top: 15px; font-size: 28px; font-weight: 400;
    letter-spacing: 7px; color: var(--orange); padding-left: 7px; line-height: 1;
  }
  .greeting__christmas {
    margin-top: 4px; font-size: 44px; font-weight: 400;
    color: var(--orange); line-height: 1; letter-spacing: 0;
  }
  .greeting__year {
    margin-top: 6px; font-size: 32px; font-weight: 300;
    letter-spacing: 11px; color: var(--orange-soft); padding-left: 11px; line-height: 1;
  }
  .wreath-photo {
    position: absolute; left: 62px; top: 234px; width: 404px; height: 410px;
    background: linear-gradient(180deg, var(--photo-tone) 0%, var(--photo-tone-deep) 100%);
  }
</style>
</head>
<body>
  <main class="card-spread">
    <section class="panel panel--inside">
      <div class="pattern-field" role="img" aria-label="Faint white snowflake pattern across the inside panel"></div>
      <div class="brand-lockup">
        <span class="brand-dot"></span>
        <span class="brand-name">Corva<br>Linde</span>
      </div>
    </section>
    <section class="panel panel--cover">
      <div class="blush-band" role="img" aria-label="Blush band with a faint snowflake pattern"></div>
      <div class="swirl-field" role="img" aria-label="Thin blush swirling line ornaments along the lower cover"></div>
      <div class="greeting">
        <p class="greeting__lead">WISHING YOU A HAPPY</p>
        <p class="greeting__merry">MERRY</p>
        <h1 class="greeting__christmas">CHRISTMAS</h1>
        <p class="greeting__year">2025</p>
      </div>
      <div class="wreath-photo" role="img" aria-label="Photograph of a live herb wreath with lavender, sage, rosemary and bay leaves hanging on a white door"></div>
    </section>
  </main>
</body>
</html>
```